Letterhead Design Project and Envelopes

MORVEN'S CLEANING SERVICES
4187 HALVERN RD. SUITE 213B
GLEN BURNIE, MD 21748

Target Market(s)

CLEANING SERVICESwww.morvenscleanpro.example

Industry/Entity Type

House Cleaning

Colors
0355a3
fbee3d
33a6d7

```html
<!DOCTYPE html>
<html lang="en">
<head>
<meta charset="utf-8">
<title>Morven's Cleaning Services – Letterhead</title>
<link href="https://fonts.googleapis.com/css2?family=Arimo:wght@400;700&display=swap" rel="stylesheet">
<style>
  :root {
    --backdrop: #d6d5d3;
    --paper: #ffffff;
    --brand-blue: #3f6fb6;
    --sky-blue: #5b8fcc;
    --pale-blue: #a9c9e8;
    --wave-blue: #86b1dd;
    --brand-yellow: #f3e33a;
    --ghost: #f4f4f4;
    --ink-light: #ffffff;
  }
  * { margin: 0; padding: 0; box-sizing: border-box; }
  html, body {
    width: 1200px; height: 1146px; overflow: hidden;
    background: var(--backdrop);
    font-family: "Arimo", Arial, sans-serif;
  }
  .stage { position: relative; width: 1200px; height: 1146px; }
  .letterhead {
    position: absolute; left: 242px; top: 110px;
    width: 896px; height: 1158px;
    background: var(--paper);
    transform: scale(0.8); transform-origin: top left;
    overflow: hidden;
  }
  .letterhead__shapes { position: absolute; inset: 0; width: 896px; height: 1158px; display: block; }
  .brand-mark {
    position: absolute; left: 0; right: 0; top: 96px;
    display: flex; justify-content: center; align-items: center; gap: 10px;
  }
  .brand-mark__dot {
    width: 18px; height: 18px; border-radius: 50%;
    background: var(--brand-yellow);
  }
  .brand-mark__name {
    font-weight: 700; font-size: 40px; line-height: 48px; color: var(--brand-blue);
  }
  .watermark {
    position: absolute; left: 0; right: 0; top: 500px;
    text-align: center;
    font-weight: 700; font-size: 150px; line-height: 180px; color: var(--ghost);
  }
  .footer-line {
    position: absolute; left: 0; right: 0; top: 1123px;
    text-align: center; color: var(--ink-light);
    font-size: 12px; line-height: 16px; white-space: nowrap;
  }
  .footer-line strong { font-weight: 700; }
</style>
</head>
<body>
<div class="stage">
  <div class="letterhead">
    <svg class="letterhead__shapes" viewBox="0 0 896 1158" preserveAspectRatio="none" aria-hidden="true">
      <rect x="0" y="0" width="896" height="100" fill="var(--brand-blue)"/>
      <path d="M0 8 C60 0 110 8 140 20 C200 8 260 22 300 36 L300 100 L0 100 Z" fill="var(--sky-blue)"/>
      <path d="M80 22 C120 15 150 40 150 72 L300 72 C260 45 200 40 180 50 C160 30 120 22 80 22 Z" fill="var(--pale-blue)"/>
      <path d="M590 22 C650 6 720 8 780 26 L800 16 C830 6 870 8 896 10 L896 100 L590 100 Z" fill="var(--sky-blue)" opacity="0.5"/>
      <path d="M0 18 C50 18 110 22 140 40 C150 58 150 68 150 72 C190 56 260 52 305 68
               C330 62 360 56 385 54 C440 50 470 52 500 48
               C560 30 620 18 680 18 C720 20 750 30 775 42
               C790 24 820 14 850 15 L896 15
               L896 1158 L0 1158 Z" fill="var(--paper)"/>
      <path d="M0 1088 C200 1078 340 1086 450 1090 C580 1080 760 1078 896 1088 L896 1158 L0 1158 Z" fill="var(--wave-blue)"/>
      <path d="M0 1106 C160 1092 320 1098 450 1100 C620 1096 780 1100 896 1116 L896 1158 L0 1158 Z" fill="var(--brand-blue)"/>
    </svg>

    <div class="brand-mark">
      <span class="brand-mark__dot"></span>
      <span class="brand-mark__name">Morven's</span>
    </div>

    <div class="watermark" aria-hidden="true">Morven's</div>

    <p class="footer-line">
      <strong>MORVEN'S CLEANING SERVICES</strong> · 4187 Halvern Rd, Ashcombe, VT 05871 · <strong>Tel:</strong> 802 555 0187 · www.morvenscleanpro.example
    </p>
  </div>
</div>
</body>
</html>
```